I am planning to launch a new online company called allphonedeskhub.net. This will be a place where people who work in call centres can come and purchase downloadable templates, tool-kits, courseware etc to help them in their jobs. The site will also share the latest information around research, best practices, news in the industry. Essentially a hub for AllPhoneDeskHub related.

I need someone to build the site for me from scratch (I have only just bought the domain name). Everything from the look and feel of the website (focus on easy to use, clean and sharp graphics, with a bit of fun), highly focused on social media and building a community, full blown e-commerce that allows for memberships/subscriptions/and one off purchase models. If you can also design custom graphics (high quality) that would be even better. Given my research of other companies in this space their websites are very dull that look like knowledge bases. I will want alot of cool visuals that attract the customers in. My initial thinking on colour scheme is bright greens/pinks/yellows etc. Not fluorescent though!

The site will contain alot of documents, templates, presentations, videos, articles, white papers etc. You must have experience in the best way to structure the site in an organised manner so that my customer can find what they need very easily.

The person who takes on this work must be happy to work collaboratively with me. It is also key that when the project is delivered that I am able to maintain alot of it myself in terms of uploading documents, blog updates, adding new products, real-time reports/analytics etc.

Whilst you are designing the website I will be working on the content so I will need your help to understand how I structure my content so that it makes sense for the design.

I will base my choice of designer on levels of experience (I will want to see previous work that you have done). I am not adverse to you using tools like shopify etc. if it meets the overall requirements of the site and adds to the functionality/look and feel.

Target Market(s)

People who work in call centres primarily those that are responsible for managing teams of the call centre itself

Industry/Entity Type

Business

Number of Pages Required

5+ page

Font styles to use
Sans Serif

Colors
33b8a4
34a6d7
886aae
b868aa
e667a6
f04a51
f68e4e
faa54b
ffcf3e

Requirements
Must have
• E-commerce functionality that allows for subscriptions and one-off payments
• Credit card processing and accept wire/bank transfers
• Easy to use layout
• Products sold alone and/or as part of bundles
• Membership area
• Front page
• About Us page
• Contact Us page
• Store page (with e-commerce back end)
• News page
• Free Resources page
• Cool, bright, fun look and feel
Nice to have
• Cool, bright, fun graphics
Should not have
• Should not look old fashioned or be difficult to navigate
• Should not look too busy or disorganised

```html
<!DOCTYPE html>
<html lang="en">
<head>
<meta charset="utf-8">
<title>AllPhoneDeskHub</title>
<link rel="stylesheet" href="https://fonts.googleapis.com/css2?family=Open+Sans:wght@300;400;600;700&display=swap">
<style>
:root{
  --green:#a6cc38;
  --green-dark:#93b92c;
  --purple:#8d6cc0;
  --orange:#f7923a;
  --ink:#2f2f2f;
  --text:#5e5e5e;
  --muted:#8a8a8a;
  --line:#e6e6e6;
  --soft:#f6f6f2;
  --panel:#f7f7f7;
  --dark:#3b3b3b;
  --footer:#0e0e0e;
  --white:#ffffff;
}
*{box-sizing:border-box;margin:0;padding:0}
html,body{width:1200px;height:2826px;overflow:hidden}
body{position:relative;background:var(--white);font-family:'Open Sans',Arial,sans-serif;color:var(--text)}
.abs{position:absolute}

/* header */
.site-header{position:absolute;left:0;top:0;width:1200px;height:102px;border-bottom:1px solid var(--line)}
.brand{position:absolute;left:132px;top:36px;font-size:23px;font-weight:600;color:var(--ink);letter-spacing:.2px}
.main-nav{position:absolute;top:42px;left:0;width:1200px;font-size:13.5px;color:var(--ink)}
.main-nav span{position:absolute;white-space:nowrap}
.main-nav .active{color:var(--green)}

/* hero */
.hero{position:absolute;left:0;top:102px;width:1200px;height:527px;background:linear-gradient(90deg,#ffffff 0%,#fbfbfb 40%,#eeeeee 60%,#e6e4e2 100%);overflow:hidden}
.hero-photo{position:absolute;left:600px;top:0;width:600px;height:527px;background:linear-gradient(90deg,rgba(245,245,245,0) 0%,#dcdad6 35%,#cfccc7 70%,#bdbab5 100%)}
.hero-title{position:absolute;left:132px;top:108px;font-size:44px;font-weight:400;color:var(--ink);line-height:54px}
.hero-title .accent{display:block;color:var(--green)}
.hero-sub{position:absolute;left:134px;top:226px;font-size:22px;color:var(--ink)}
.hero-copy{position:absolute;left:134px;top:266px;width:470px;font-size:14px;line-height:25px;color:var(--ink)}
.btn-start{position:absolute;left:132px;top:374px;width:175px;height:46px;background:var(--green);color:var(--white);font-size:12px;font-weight:600;display:flex;align-items:center;justify-content:center;border-radius:2px;letter-spacing:.3px}
.dots{position:absolute;left:572px;top:480px}
.dots i{position:absolute;top:0;width:13px;height:13px;border-radius:50%;border:2px solid var(--green)}
.dots i.on{background:var(--green)}

/* categories */
.categories{position:absolute;left:132px;top:691px;width:233px;background:var(--panel)}
.categories h3{height:55px;background:var(--green);color:var(--white);font-size:17px;font-weight:400;padding:16px 26px}
.categories ul{list-style:none;padding:0 14px 10px 14px}
.categories li{height:49.5px;border-bottom:1px solid var(--line);font-size:13px;color:var(--ink);display:flex;align-items:center;justify-content:space-between;padding-left:12px}
.categories li:last-child{border-bottom:none}
.categories li b{font-weight:400;color:#bbb;font-size:13px}

/* services */
.service{position:absolute;width:240px;text-align:center}
.service .ring{width:160px;height:160px;margin:0 auto;border-radius:50%;border:4px solid #ececec;display:flex;align-items:center;justify-content:center}
.service .ring svg{width:152px;height:152px}
.service p{margin-top:16px;font-size:14px;line-height:22px;color:var(--muted)}

/* about */
.about{position:absolute;left:0;top:1483px;width:1200px;height:339px;background:var(--soft)}
.about h2{position:absolute;left:130px;top:62px;font-size:27px;font-weight:600;color:var(--ink)}
.about .copy{position:absolute;left:131px;top:110px;width:518px;font-size:12.5px;line-height:23px;color:var(--text)}
.about .copy p+p{margin-top:23px}
.video{position:absolute;left:688px;top:68px;width:380px;height:209px;background:linear-gradient(135deg,#6f7a84 0%,#3f4851 50%,#252b31 100%);overflow:hidden}
.video .controls{position:absolute;left:0;bottom:0;width:100%;height:24px;background:#1b1b1b}

/* products */
.products{position:absolute;left:0;top:1822px;width:1200px;height:394px;background:var(--green)}
.products h2{position:absolute;left:0;top:46px;width:1200px;text-align:center;font-size:26px;font-weight:600;color:var(--white)}
.products .lead{position:absolute;left:0;top:84px;width:1200px;text-align:center;font-size:19px;color:var(--white)}
.product{position:absolute;top:130px;width:240px;text-align:center}
.product .thumb{width:172px;height:172px;margin:0 auto;border-radius:50%;border:5px solid var(--white)}
.product p{margin-top:14px;font-size:17px;color:var(--white)}

/* blog */
.blog-title{position:absolute;left:130px;top:2264px;font-size:27px;font-weight:600;color:var(--ink)}
.arrow-btn{position:absolute;top:2274px;width:27px;height:27px;border-radius:50%;border:1px solid #bdbdbd}
.post{position:absolute;top:2321px;width:292px}
.post .image{height:125px;background:linear-gradient(135deg,#e7ecef 0%,#bcc6cd 55%,#8e99a1 100%)}
.post h4{margin-top:17px;font-size:18px;font-weight:400;color:var(--ink)}
.post .meta{margin-top:2px;font-size:10.5px;font-weight:600;color:var(--green)}
.post .excerpt{margin-top:8px;font-size:11.5px;line-height:19px;color:var(--text);text-align:justify}
.share{display:flex;gap:6px;margin-top:10px;height:12px}
.share i{display:block;height:12px;border:1px solid #cfd6e3;border-radius:2px;background:#eef2f8}
.btn-more{margin-top:18px;width:103px;height:32px;background:var(--dark);color:var(--white);font-size:11.5px;display:flex;align-items:center;justify-content:center;border-radius:2px}

/* footer */
.site-footer{position:absolute;left:0;top:2706px;width:1200px;height:120px;background:var(--footer);color:#cfcfcf}
.footer-links{position:absolute;left:132px;top:44px;font-size:12px;color:#d8d8d8}
.copyright{position:absolute;left:132px;top:66px;font-size:12px;color:#bdbdbd}
.news-label{position:absolute;left:433px;top:39px;font-size:12px;color:#d8d8d8}
.news-input{position:absolute;left:433px;top:60px;width:144px;height:22px;background:#e8e8e8;font-size:10px;color:#999;padding:4px 6px}
.news-btn{position:absolute;left:577px;top:60px;width:60px;height:22px;background:var(--green-dark);color:var(--white);font-size:10px;display:flex;align-items:center;justify-content:center}
.call{position:absolute;left:709px;top:40px}
.call small{position:absolute;left:45px;top:0;font-size:11px;color:#9a9a9a;white-space:nowrap}
.call strong{position:absolute;left:45px;top:14px;font-size:19px;font-weight:400;color:#e0e0e0;white-space:nowrap}
.social i{position:absolute;top:51px;width:24px;height:24px;border-radius:50%;background:#5a5a5a}
</style>
</head>
<body>

<header class="site-header">
  <div class="brand">AllPhoneDeskHub</div>
  <nav class="main-nav">
    <span class="active" style="left:519px">Home</span>
    <span style="left:600px">About us</span>
    <span style="left:698px">News</span>
    <span style="left:776px">Free Stuff</span>
    <span style="left:881px">Membership</span>
    <span style="left:1000px">Contact us</span>
  </nav>
</header>

<section class="hero">
  <div class="hero-photo" role="img" aria-label="Smiling call centre agent wearing a headset in a bright office"></div>
  <h1 class="hero-title">Welcome to<span class="accent">AllPhoneDeskHub</span></h1>
  <div class="hero-sub">Duis aute irure dolor in reprehenderit&nbsp; velit</div>
  <p class="hero-copy">sed do eiusmod tempor incididunt ut labore et dolore magna aliqua. Ut enim ad minim veniam, quis nostrud exercitation ullamco laboris nisi ut aliquip ex ea commodo consequat.</p>
  <div class="btn-start">GET STARTED NOW !</div>
  <div class="dots"><i style="left:0"></i><i class="on" style="left:19px"></i><i style="left:38px"></i></div>
</section>

<aside class="categories">
  <h3>Categories</h3>
  <ul>
    <li>Sed ut perspiciatis unde<b>›</b></li>
    <li>Omnis iste natus error sit<b>›</b></li>
    <li>Voluptatem accusantium<b>›</b></li>
    <li>Doloremque laudantium<b>›</b></li>
    <li>Totam rem aperiam, eaque<b>›</b></li>
    <li>Ipsa quae ab illo inventore<b>›</b></li>
    <li>Veritatis et quasi archite<b>›</b></li>
    <li>Beatae vitae dicta sunt<b>›</b></li>
    <li>Explicabo nemo enim<b>›</b></li>
    <li>Dit aut fugit sed quia<b>›</b></li>
    <li>Consequntur magni<b>›</b></li>
    <li>Dolores eos qui ratione<b>›</b></li>
  </ul>
</aside>

<div class="service" style="left:396px;top:691px">
  <div class="ring"><svg viewBox="0 0 152 152"><circle cx="76" cy="76" r="76" fill="var(--green)"/><g fill="#fff"><rect x="48" y="82" width="10" height="22"/><rect x="63" y="74" width="10" height="30"/><rect x="78" y="66" width="10" height="38"/><rect x="93" y="58" width="10" height="46"/><rect x="44" y="104" width="64" height="3"/></g><path d="M48 72 L70 56 L82 62 L102 44" stroke="#fff" stroke-width="4" fill="none"/><path d="M96 42 L106 40 L104 50 Z" fill="#fff"/></svg></div>
  <p>Performance Mesurement &amp;<br>Management</p>
</div>
<div class="service" style="left:628px;top:691px">
  <div class="ring"><svg viewBox="0 0 152 152"><circle cx="76" cy="76" r="76" fill="var(--green)"/><path d="M60 48 H92 V62 Q92 82 76 84 Q60 82 60 62 Z" fill="#fff"/><rect x="72" y="84" width="8" height="12" fill="#fff"/><rect x="62" y="96" width="28" height="8" fill="#fff"/><path d="M54 52 Q40 70 56 90 M98 52 Q112 70 96 90" stroke="#fff" stroke-width="3" fill="none"/></svg></div>
  <p>Morale and Motivation</p>
</div>
<div class="service" style="left:867px;top:691px">
  <div class="ring"><svg viewBox="0 0 152 152"><circle cx="76" cy="76" r="76" fill="var(--green)"/><rect x="44" y="60" width="38" height="30" fill="#fff"/><rect x="49" y="74" width="5" height="10" fill="var(--green)"/><rect x="58" y="68" width="5" height="16" fill="var(--green)"/><rect x="67" y="64" width="5" height="20" fill="var(--green)"/><circle cx="96" cy="58" r="11" fill="#fff"/><path d="M80 100 Q80 74 96 74 Q112 74 112 100 Z" fill="#fff"/><rect x="40" y="100" width="74" height="4" fill="#fff"/></svg></div>
  <p>Coaching and Mentoring</p>
</div>

<div class="service" style="left:396px;top:956px">
  <div class="ring"><svg viewBox="0 0 152 152"><circle cx="76" cy="76" r="76" fill="var(--purple)"/><rect x="48" y="44" width="44" height="32" fill="none" stroke="#fff" stroke-width="4"/><path d="M54 68 L64 58 L72 64 L84 52" stroke="#fff" stroke-width="3" fill="none"/><circle cx="104" cy="60" r="7" fill="#fff"/><rect x="98" y="70" width="12" height="24" fill="#fff"/><circle cx="60" cy="90" r="6" fill="#fff"/><circle cx="80" cy="90" r="6" fill="#fff"/><path d="M50 108 Q50 96 60 96 Q70 96 70 108 Z M70 108 Q70 96 80 96 Q90 96 90 108 Z" fill="#fff"/></svg></div>
  <p>Leadership and Management</p>
</div>
<div class="service" style="left:628px;top:956px">
  <div class="ring"><svg viewBox="0 0 152 152"><circle cx="76" cy="76" r="76" fill="var(--purple)"/><circle cx="76" cy="52" r="8" fill="#fff"/><path d="M64 76 Q64 62 76 62 Q88 62 88 76 Z" fill="#fff"/><rect x="56" y="76" width="40" height="18" fill="#fff"/><rect x="44" y="94" width="64" height="8" fill="#fff"/><rect x="38" y="102" width="76" height="6" fill="#fff"/></svg></div>
  <p>Reward and Recognition</p>
</div>
<div class="service" style="left:867px;top:956px">
  <div class="ring"><svg viewBox="0 0 152 152"><circle cx="76" cy="76" r="76" fill="var(--purple)"/><path d="M50 108 Q50 84 76 84 Q102 84 102 108 Z" fill="#fff"/><circle cx="76" cy="64" r="16" fill="#fff"/><path d="M56 64 Q56 40 76 40 Q96 40 96 64" stroke="#fff" stroke-width="4" fill="none"/><rect x="51" y="58" width="8" height="14" rx="3" fill="#fff"/><rect x="93" y="58" width="8" height="14" rx="3" fill="#fff"/></svg></div>
  <p>Communication Skills</p>
</div>

<div class="service" style="left:396px;top:1211px">
  <div class="ring"><svg viewBox="0 0 152 152"><circle cx="76" cy="76" r="76" fill="var(--orange)"/><path d="M50 46 L60 92 H94" stroke="#fff" stroke-width="5" fill="none"/><rect x="58" y="92" width="6" height="16" fill="#fff"/><circle cx="88" cy="62" r="9" fill="#fff"/><path d="M74 92 Q74 74 88 74 Q102 74 102 92 Z" fill="#fff"/><path d="M80 62 Q80 50 88 50 Q96 50 96 62" stroke="#fff" stroke-width="3" fill="none"/></svg></div>
  <p>Call Centre Technology</p>
</div>
<div class="service" style="left:628px;top:1211px">
  <div class="ring"><svg viewBox="0 0 152 152"><circle cx="76" cy="76" r="76" fill="var(--orange)"/><circle cx="64" cy="56" r="11" fill="none" stroke="#fff" stroke-width="5" stroke-dasharray="5 3"/><circle cx="88" cy="48" r="8" fill="none" stroke="#fff" stroke-width="4" stroke-dasharray="4 3"/><circle cx="80" cy="80" r="12" fill="#fff"/><path d="M58 112 Q58 92 80 92 Q102 92 102 112 Z" fill="#fff"/></svg></div>
  <p>Call Centre Strategy</p>
</div>
<div class="service" style="left:867px;top:1211px">
  <div class="ring"><svg viewBox="0 0 152 152"><circle cx="76" cy="76" r="76" fill="var(--orange)"/><rect x="50" y="70" width="9" height="30" fill="#fff"/><rect x="63" y="56" width="9" height="44" fill="#fff"/><rect x="76" y="78" width="9" height="22" fill="#fff"/><circle cx="92" cy="72" r="12" fill="none" stroke="#fff" stroke-width="5"/><path d="M100 82 L110 96" stroke="#fff" stroke-width="6"/><rect x="44" y="100" width="50" height="4" fill="#fff"/></svg></div>
  <p>Research and Best<br>Practices</p>
</div>

<section class="about">
  <h2>About AllPhoneDeskHub</h2>
  <div class="copy">
    <p>Lorem Ipsum is simply dummy text of the printing and typesetting industry. Lorem Ipsum has been the industry's standard dummy text ever since the 1500s, when an unknown printer took a galley of type and scrambled it to make a type specimen book.</p>
    <p>Lorem Ipsum is simply dummy text of the printing and typesetting industry. Lorem Ipsum has been the industry's standard dummy text ever since the 1500s, when an unknown printer took a galley of type and scrambled it to make a type specimen book.</p>
  </div>
  <div class="video" role="img" aria-label="Video: team of call centre agents with headsets at their desks">
    <svg class="abs" style="left:159px;top:75px" width="60" height="60" viewBox="0 0 60 60"><circle cx="30" cy="30" r="28" fill="#111" fill-opacity=".75" stroke="#fff" stroke-width="3"/><path d="M24 18 L42 30 L24 42 Z" fill="#fff"/></svg>
    <div class="controls">
      <svg class="abs" style="left:8px;top:7px" width="80" height="10" viewBox="0 0 80 10"><path d="M0 0 L8 5 L0 10 Z" fill="#ccc"/><path d="M22 3 H26 L30 0 V10 L26 7 H22 Z" fill="#ccc"/><text x="44" y="9" font-size="9" fill="#ccc" font-family="Open Sans, sans-serif">0:00</text></svg>
      <svg class="abs" style="left:300px;top:6px" width="72" height="12" viewBox="0 0 72 12"><circle cx="6" cy="6" r="4" fill="none" stroke="#ccc" stroke-width="2"/><rect x="22" y="2" width="22" height="8" rx="2" fill="#666"/><path d="M56 1 H62 M56 1 V5 M70 1 H66 M70 1 V5 M56 11 V7 M56 11 H60 M70 11 V7 M70 11 H66" stroke="#ccc" stroke-width="1.5"/></svg>
    </div>
  </div>
</section>

<section class="products">
  <h2>Our Products</h2>
  <p class="lead">Reprehenderit in voluptate velit esse cillum dolore eu fugiat nulla pariatur excepteur</p>
  <div class="product" style="left:132px"><div class="thumb" role="img" aria-label="Colourful stacked infographic template" style="background:linear-gradient(180deg,#7fa7b8 0%,#d9c6a4 40%,#8a6a58 62%,#e8574a 82%,#f1eee8 100%)"></div><p>Templates</p></div>
  <div class="product" style="left:366px"><div class="thumb" role="img" aria-label="Agent working at a computer with a headset" style="background:linear-gradient(135deg,#e8edf0 0%,#b8c2c9 55%,#6f7a84 100%)"></div><p>Tool- Kits</p></div>
  <div class="product" style="left:598px"><div class="thumb" role="img" aria-label="Close-up of a desk phone keypad" style="background:linear-gradient(135deg,#f2f2f2 0%,#b9b9b9 50%,#5d5d5d 100%)"></div><p>Courceware</p></div>
  <div class="product" style="left:837px"><div class="thumb" role="img" aria-label="Call centre agent speaking into a headset" style="background:linear-gradient(135deg,#dfe3e6 0%,#b79c8a 55%,#4e4a48 100%)"></div><p>Communication Skills</p></div>
</section>

<h2 class="blog-title">Latest Blog</h2>
<svg class="arrow-btn" style="left:1010px" viewBox="0 0 27 27"><path d="M15 8 L10 13.5 L15 19" stroke="#999" stroke-width="2" fill="none"/></svg>
<svg class="arrow-btn" style="left:1042px" viewBox="0 0 27 27"><path d="M12 8 L17 13.5 L12 19" stroke="#999" stroke-width="2" fill="none"/></svg>

<article class="post" style="left:132px">
  <div class="image" role="img" aria-label="Row of call centre agents with headsets at computers"></div>
  <h4>AllPhoneDeskHub</h4>
  <div class="meta">by Admin - November 12, 2015</div>
  <p class="excerpt">Lorem Ipsum is simply dummy text of the printing and typesetting industry. Lorem Ipsum has been the industry's standard dummy text</p>
  <div class="share"><i style="width:30px"></i><i style="width:14px"></i><i style="width:34px"></i><i style="width:14px"></i><i style="width:30px"></i><i style="width:14px"></i></div>
  <div class="btn-more">READ MORE</div>
</article>
<article class="post" style="left:454px">
  <div class="image" role="img" aria-label="Agent with a headset in an open plan office" style="background:linear-gradient(135deg,#eef0f1 0%,#c9bfb5 50%,#7f8890 100%)"></div>
  <h4>AllPhoneDeskHub</h4>
  <div class="meta">by Admin - November 12, 2015</div>
  <p class="excerpt">Lorem Ipsum is simply dummy text of the printing and typesetting industry. Lorem Ipsum has been the industry's standard dummy text</p>
  <div class="share"><i style="width:30px"></i><i style="width:14px"></i><i style="width:34px"></i><i style="width:14px"></i><i style="width:30px"></i><i style="width:14px"></i></div>
  <div class="btn-more">READ MORE</div>
</article>
<article class="post" style="left:776px">
  <div class="image" role="img" aria-label="Group of call centre agents wearing headsets" style="background:linear-gradient(135deg,#f0f1f2 0%,#c4c9cd 50%,#5f666d 100%)"></div>
  <h4>AllPhoneDeskHub</h4>
  <div class="meta">by Admin - November 12, 2015</div>
  <p class="excerpt">Lorem Ipsum is simply dummy text of the printing and typesetting industry. Lorem Ipsum has been the industry's standard dummy text</p>
  <div class="share"><i style="width:30px"></i><i style="width:14px"></i><i style="width:34px"></i><i style="width:14px"></i><i style="width:30px"></i><i style="width:14px"></i></div>
  <div class="btn-more">READ MORE</div>
</article>

<footer class="site-footer">
  <div class="footer-links">About&nbsp; | &nbsp;Terms&nbsp; | &nbsp;Privacy Policy</div>
  <div class="copyright">All Rights Reserved. Copyrights © 2015.</div>
  <div class="news-label">Newsletter Signup</div>
  <div class="news-input">Email Address</div>
  <div class="news-btn">Subscribe</div>
  <div class="call">
    <svg width="36" height="36" viewBox="0 0 36 36"><circle cx="18" cy="18" r="16" fill="none" stroke="#8a8a8a" stroke-width="2"/><path d="M12 10 Q10 12 11 16 Q14 23 20 25 Q24 26 26 24 L23 20 L20 21 Q16 19 15 15 L16 12 Z" fill="#8a8a8a"/></svg>
    <small>Call Us:</small>
    <strong>01-555-0142</strong>
  </div>
  <div class="social"><i style="left:939px"></i><i style="left:973px"></i><i style="left:1007px"></i><i style="left:1041px"></i></div>
</footer>

</body>
</html>
```